ReelVows Identity
Pamphlet/Business Cards
@PH - please check your private message on top right once you login to your pixelhive account & reply.
Thanks
Hi, I like the card on top, but please don't include my contact info...
It should include things like "Toronto, Montreal, Ottawa, Vancouver, Calgary, Edmonton", website reelvows.ca, phone 1.877.555.0148, email info@reelvows-example.ca and facebook www.facebook.com/reelvows
We need a business card and 4x6 pamphlet designs, styled similar to our website http://reelvows-example.ca

```html
<!DOCTYPE html>
<html lang="en">
<head>
<meta charset="utf-8">
<title>ReelVows Identity – Pamphlet and Business Cards</title>
<link rel="stylesheet" href="https://fonts.googleapis.com/css2?family=Source+Sans+3:wght@400;600;700&display=swap">
<style>
:root{
  --stage:#e9e4de;
  --ink:#0b0b0b;
  --panel:#161616;
  --white:#ffffff;
  --muted:#b9b9b9;
  --accent:#f0801e;
  --silver-a:#f4f4f4;
  --silver-b:#a9a9a9;
  --photo-a:#d9d2cb;
  --photo-b:#5a4a44;
}
*{box-sizing:border-box;margin:0;padding:0}
html,body{width:1200px;height:631px;overflow:hidden;background:var(--stage);font-family:"Source Sans 3",Arial,sans-serif;color:var(--white)}
.canvas{position:relative;width:1200px;height:631px}
.flyer{position:absolute;top:16px;width:380px;height:599px;background:radial-gradient(ellipse at 50% 20%,#222 0%,var(--ink) 65%);box-shadow:0 3px 10px rgba(0,0,0,.25);overflow:hidden}
.flyer-front{left:30px}
.flyer-back{left:432px}
.brand{display:flex;flex-direction:column;align-items:center;gap:5px}
.brand-mark{width:34px;height:34px;border:2px solid var(--white);border-radius:50%}
.brand-name{font-weight:600;font-size:17px;letter-spacing:3px;text-transform:uppercase;color:var(--white)}
.flyer .brand{position:absolute;top:26px;left:0;right:0}
.top-contact{position:absolute;top:24px;right:18px;font-size:8px;line-height:13px;color:var(--muted);text-align:right}
.headline{position:absolute;left:0;right:0;text-align:center;font-weight:600;font-size:21px;line-height:24px}
.headline .plus{color:var(--accent)}
.flyer-front .headline{top:112px}
.photo{position:absolute;left:20px;right:20px;top:170px;height:258px;background:linear-gradient(135deg,var(--photo-a) 0%,#a8988e 45%,var(--photo-b) 100%)}
.cities{position:absolute;left:0;right:0;top:440px;text-align:center;font-size:9px;letter-spacing:.5px;color:var(--white)}
.offer{position:absolute;left:0;right:0;top:488px;text-align:center;font-weight:700;font-size:13px;line-height:17px;color:var(--accent)}
.facebook{position:absolute;left:0;right:0;top:533px;text-align:center;font-size:9px;color:var(--muted)}
.contact-bar{position:absolute;left:0;right:0;bottom:0;height:34px;background:var(--panel);border-top:1px solid #333;display:flex;justify-content:space-around;align-items:center;font-size:10px;color:var(--white)}
.contact-bar b{color:var(--accent);font-weight:600;font-size:12px}
.city-box{position:absolute;top:20px;right:18px;border:1px solid #555;padding:5px 8px;font-size:8px;line-height:10px;color:var(--muted)}
.flyer-back .brand{left:-40px}
.flyer-back .headline{top:104px}
.packages{position:absolute;left:26px;right:22px;top:168px}
.packages h2{font-size:12px;font-weight:700;color:var(--accent);letter-spacing:.3px;margin-bottom:4px}
.packages p{font-size:8px;color:var(--white);margin-bottom:3px}
.packages ul{list-style:none;margin-bottom:12px}
.packages li{font-size:8px;line-height:12px;color:var(--muted)}
.packages li::before{content:"\2022 ";color:var(--accent)}
.portraits{position:absolute;left:0;right:0;top:478px;display:flex;justify-content:center;gap:12px}
.portrait{width:50px;height:50px;border-radius:50%;border:2px solid var(--white);background:radial-gradient(circle at 40% 40%,var(--photo-a),var(--photo-b))}
.card{position:absolute;left:842px;width:326px;height:188px;box-shadow:0 3px 10px rgba(0,0,0,.25);overflow:hidden}
.card-front{top:60px;background:linear-gradient(180deg,var(--silver-a) 0%,#d6d6d6 55%,var(--silver-b) 100%);color:var(--ink)}
.card-front .card-top{height:22px;background:var(--ink);color:var(--white);font-size:8px;line-height:22px;padding-left:14px}
.card-front .brand{position:absolute;top:44px;left:0;right:0}
.card .brand-mark{border-color:var(--ink)}
.card .brand-name{color:var(--ink);font-size:15px}
.card-details{position:absolute;left:14px;right:14px;bottom:14px;display:flex;justify-content:space-between;font-size:7.5px;line-height:11px;color:#333}
.card-back{top:270px;background:var(--white);color:var(--ink)}
.card-back .brand{position:absolute;top:50px;left:0;right:0}
.card-back .site{position:absolute;bottom:14px;left:0;right:0;text-align:center;font-size:8px;color:#555}
</style>
</head>
<body>
<main class="canvas">

  <article class="flyer flyer-front">
    <div class="top-contact">t 1 416 555 0172<br>f 1 416 555 0179</div>
    <div class="brand"><span class="brand-mark"></span><span class="brand-name">ReelVows</span></div>
    <h1 class="headline">Videography <span class="plus">+</span> Photography<br>packages starting at $1,995</h1>
    <div class="photo" role="img" aria-label="Wedding photo of a bride holding a bouquet"></div>
    <p class="cities">Toronto &nbsp;|&nbsp; Montreal &nbsp;|&nbsp; Ottawa &nbsp;|&nbsp; Vancouver &nbsp;|&nbsp; Calgary &nbsp;|&nbsp; Edmonton</p>
    <p class="offer">BOOK VIDEOGRAPHY AND PHOTOGRAPHY<br>TOGETHER AND GET 10% OFF</p>
    <p class="facebook">www.facebook.com/reelvows</p>
    <div class="contact-bar"><span>call us <b>1.877.555.0148</b></span><span>email info@reelvows-example.ca</span></div>
  </article>

  <article class="flyer flyer-back">
    <div class="city-box">Toronto<br>Montreal<br>Ottawa<br>Vancouver<br>Calgary<br>Edmonton</div>
    <div class="brand"><span class="brand-mark"></span><span class="brand-name">ReelVows</span></div>
    <h1 class="headline">Videography <span class="plus">+</span> Photography<br>packages starting at $1,995</h1>
    <section class="packages">
      <h2>WEDDING VIDEOGRAPHY PACKAGES</h2>
      <p>All of our videography packages include:</p>
      <ul>
        <li>Videos recorded in 1080p HD using modern twin camera setups</li>
        <li>Ceremony and reception filmed with wireless audio capture</li>
        <li>Creative cinematic editing with licensed music tracks</li>
        <li>Locations included: bride preparations, ceremony, portraits</li>
        <li>Highlight reel delivered within six weeks of event</li>
        <li>Full length feature film on custom DVD</li>
        <li>Online streaming link shared with family and friends</li>
      </ul>
      <h2>WEDDING PHOTOGRAPHY PACKAGES</h2>
      <p>All of our photography packages include:</p>
      <ul>
        <li>Unlimited number of photos taken</li>
        <li>Complete coverage during the selected timeframe</li>
        <li>All photos are colour corrected and delivered on DVD</li>
        <li>A private online gallery with easy sharing</li>
        <li>Print release included for every final image</li>
      </ul>
    </section>
    <div class="portraits">
      <span class="portrait" role="img" aria-label="Round wedding photo"></span>
      <span class="portrait" role="img" aria-label="Round wedding photo"></span>
      <span class="portrait" role="img" aria-label="Round wedding photo"></span>
      <span class="portrait" role="img" aria-label="Round wedding photo"></span>
      <span class="portrait" role="img" aria-label="Round wedding photo"></span>
    </div>
    <div class="contact-bar"><span>call us <b>1.877.555.0148</b></span><span>email info@reelvows-example.ca</span></div>
  </article>

  <article class="card card-front">
    <div class="card-top">Toronto, Montreal, Ottawa, Vancouver, Calgary, Edmonton</div>
    <div class="brand"><span class="brand-mark"></span><span class="brand-name">ReelVows</span></div>
    <div class="card-details">
      <span>t 1.877.555.0148<br>e info@reelvows-example.ca<br>w www.reelvows.ca</span>
      <span>www.facebook.com/reelvows</span>
    </div>
  </article>

  <article class="card card-back">
    <div class="brand"><span class="brand-mark"></span><span class="brand-name">ReelVows</span></div>
    <p class="site">www.reelvows.ca</p>
  </article>

</main>
</body>
</html>
```